Clear Coat 5L & 2.5L kit

Clear coat 5 Liter with 2.5 Liter hardener
I attached few examples
Required size:
5L
Actual size is: 22.875 x 10.4375 inch
With bleed added: 23.125 x 10.6875 inch
2.5L
Actual size is: 22.875 x 6.1875 inch
With bleed added: 23.125x6.2125 inch

Thanks

```html
<!DOCTYPE html>
<html lang="en">
<head>
<meta charset="utf-8">
<title>Apex Hardener Label</title>
<link rel="stylesheet" href="https://fonts.googleapis.com/css2?family=Teko:wght@400;500;600&display=swap">
<style>
  :root {
    --bg: #eef02a;
    --gold: #c9a227;
    --black: #2a2a2a;
    --band: #1e1e1e;
    --white: #f4f4f4;
  }
  * { margin: 0; padding: 0; box-sizing: border-box; }
  html, body { width: 1200px; height: 687px; overflow: hidden; }
  body {
    background: var(--bg);
    font-family: "Teko", "Arial Narrow", sans-serif;
    display: flex; align-items: center; justify-content: center;
  }
  .label {
    position: relative;
    width: 1100px; height: 502px;
    background: var(--black);
    overflow: hidden;
  }
  .label__shapes { position: absolute; inset: 0; }
  .brand {
    position: absolute; left: 90px; top: 200px;
    color: var(--black);
    font-size: 80px; font-weight: 600; line-height: 1;
    text-transform: uppercase; letter-spacing: 2px;
  }
  .product {
    position: absolute; right: 120px; top: 70px;
    color: var(--white);
  }
  .product__name {
    font-size: 170px; font-weight: 600; line-height: 0.8;
    letter-spacing: 6px; text-transform: uppercase;
  }
  .product__type {
    font-size: 40px; font-weight: 400; line-height: 1;
    letter-spacing: 2px; text-transform: uppercase; margin-top: 14px;
  }
  .product__speed {
    font-size: 72px; font-weight: 500; line-height: 0.9;
    color: var(--gold); text-transform: uppercase; letter-spacing: 3px;
    margin-top: 8px;
  }
  .product__ratio {
    font-size: 40px; font-weight: 400; letter-spacing: 2px;
    text-transform: uppercase; line-height: 1;
  }
  .product__stars { display: flex; gap: 22px; margin-top: 14px; }
  .product__stars svg { width: 24px; height: 24px; fill: var(--gold); }
</style>
</head>
<body>
  <div class="label">
    <svg class="label__shapes" viewBox="0 0 1100 502" preserveAspectRatio="none" aria-hidden="true">
      <polygon points="0,0 470,0 600,502 0,502" fill="#c9a227"/>
      <rect x="0" y="0" width="40" height="502" fill="#1e1e1e"/>
      <rect x="1060" y="0" width="40" height="502" fill="#1e1e1e"/>
    </svg>

    <div class="brand">Kestrel</div>

    <div class="product">
      <div class="product__name">Apex</div>
      <div class="product__type">Hardener for<br>Clear Coat</div>
      <div class="product__speed">Slow</div>
      <div class="product__ratio">2.1 VOC / 2.1 Mix</div>
      <div class="product__stars">
        <svg viewBox="0 0 24 24"><polygon points="12,1 15,9 23,9 16.5,14 19,22 12,17 5,22 7.5,14 1,9 9,9"/></svg>
        <svg viewBox="0 0 24 24"><polygon points="12,1 15,9 23,9 16.5,14 19,22 12,17 5,22 7.5,14 1,9 9,9"/></svg>
        <svg viewBox="0 0 24 24"><polygon points="12,1 15,9 23,9 16.5,14 19,22 12,17 5,22 7.5,14 1,9 9,9"/></svg>
        <svg viewBox="0 0 24 24"><polygon points="12,1 15,9 23,9 16.5,14 19,22 12,17 5,22 7.5,14 1,9 9,9"/></svg>
      </div>
    </div>
  </div>
</body>
</html>
```